New E-Learning Website Design Wanted!

I am creating an E-learning website for those interested in getting certifications in the IT industry.
For example, courses related to VKT, Lomen, RJV certifications and national certifications in the IT industry in Japan will be offered.
You can think of sites such as Pindolia, Kestova, BrickSage, Minotell.
But I am targeting industries in Japan at the moment.
Also, I have uploaded screenshots of pages that I think are good.

The company is Velmont Data
I recently got my company logo designed so I attached pdf file to this project brief.
I would appreciate it if you can make the site match the color scheme of the logo.

Target Market(s)

I am targeting individuals as well as large IT companies in Japan

Industry/Entity Type

Education

Coding

Coded - Design and coding required

Number of Pages Required

4 page

Font styles to use
Sans Serif

Colors

Designer to choose colors to be used in the design.

Requirements
Must have
• One top page design
• One course page (https://tivokhub.example/courses/vkt-hosting-services)
• One learning page(where the learner can see the video)
• One blog page(https://info.tivokhub.example/resources?_ga=2.51827364.27461930.1629384756-830152947.1629384756)
Nice to have
• Pricing page

```html
<!DOCTYPE html>
<html lang="en">
<head>
<meta charset="utf-8">
<title>Velmont Data – Cloud Learning</title>
<link href="https://fonts.googleapis.com/css2?family=Roboto:wght@400;500;700&display=swap" rel="stylesheet">
<style>
:root{
  --navy:#1b2a55;
  --navy-btn:#1c2d5c;
  --teal:#26a699;
  --teal-dark:#1f9a8e;
  --footer:#25a497;
  --hero-bg:#dbe7fb;
  --mint:#eaf8f4;
  --steel:#2d6590;
  --link-blue:#2c5f93;
  --text:#22304d;
  --white:#ffffff;
}
*{box-sizing:border-box;margin:0;padding:0}
html,body{width:1200px;height:3425px;overflow:hidden}
body{position:relative;font-family:'Roboto',sans-serif;color:var(--text);background:var(--white)}
.abs{position:absolute}
a{color:inherit;text-decoration:none}

/* header */
.hero{left:0;top:0;width:1200px;height:712px;background:var(--hero-bg);overflow:hidden}
.brand{left:38px;top:96px;display:flex;align-items:center;gap:10px;font-size:26px;font-weight:500;color:var(--navy)}
.brand-mark{width:16px;height:16px;background:var(--navy)}
.nav{left:354px;top:56px;font-size:21px;font-weight:500;color:var(--navy)}
.nav a{position:absolute;white-space:nowrap}
.btn-sign{top:50px;height:39px;border-radius:5px;font-size:20px;color:var(--white);display:flex;align-items:center;justify-content:center}
.btn-signin{left:963px;width:95px;background:var(--navy-btn)}
.btn-signup{left:1078px;width:94px;background:var(--teal)}
.hero-title{left:40px;top:240px;font-size:40px;line-height:60px;font-weight:700;color:var(--navy)}
.hero-sub{left:40px;top:362px;font-size:19px;line-height:23px;color:var(--navy)}
.hero-label{left:40px;top:499px;font-size:18px;color:var(--navy)}
.btn-teal{background:var(--teal);color:var(--white);border-radius:4px;display:flex;align-items:center;justify-content:center}
.hero-cta{left:38px;top:533px;width:275px;height:54px;font-size:20px;font-weight:500}
.hero-art{left:540px;top:126px;width:650px;height:540px;border-radius:40px 40px 0 0;background:linear-gradient(160deg,#b9cff6 0%,#9fbcf0 45%,#8fd9c2 100%);opacity:.9}
.hero-wave{left:0;top:560px}

/* individual */
.indiv-art{left:0;top:865px;width:552px;height:305px;background:linear-gradient(180deg,#d6f3ea 0%,#a9e6d4 60%,#2fae9d 100%)}
.indiv-title{left:605px;top:805px;font-size:40px;font-weight:700;color:var(--navy)}
.indiv-text{left:605px;top:874px;width:535px;font-size:19px;line-height:26px;color:var(--link-blue)}
.checks{list-style:none;font-size:19px;color:var(--navy)}
.checks li{display:flex;align-items:center;height:36px}
.checks svg{flex:none;margin-right:30px}
.indiv-list{left:605px;top:994px}
.indiv-cta{left:607px;top:1208px;width:292px;height:56px;font-size:20px}

/* tracks */
.tracks-band{left:0;top:1380px}
.track-head{top:1385px;font-size:29px;font-weight:700;color:var(--navy);white-space:nowrap}
.card{top:1450px;width:378px;height:536px;background:var(--white);box-shadow:0 0 10px rgba(30,60,90,.12);border-radius:3px}
.card-art{position:absolute;left:25px;top:23px;width:328px;height:166px;border:1px solid #9fd8cd;border-radius:6px}
.card .checks{position:absolute;left:25px;top:225px;font-size:17px;line-height:36px}
.card .checks li{align-items:flex-start;height:auto}
.card .checks svg{margin:10px 22px 0 0}
.card-btn{position:absolute;left:98px;top:471px;width:175px;height:49px;font-size:19px}

/* success */
.success-title{left:0;width:1200px;top:2110px;text-align:center;font-size:40px;font-weight:700;color:var(--navy)}
.quote-card{top:2206px;width:451px;height:428px;background:var(--white);box-shadow:0 0 10px rgba(30,60,90,.12);overflow:hidden;border-radius:3px}
.quote-title{position:absolute;left:0;width:100%;top:28px;text-align:center;font-size:30px;line-height:41px;font-weight:700;color:var(--navy)}
.quote-text{position:absolute;left:70px;width:340px;top:140px;font-size:20px;line-height:37px;color:var(--navy)}
.quote-wave{position:absolute;left:0;top:295px}
.avatar{position:absolute;left:19px;top:347px;width:62px;height:62px;border-radius:50%;background:var(--white);display:flex;align-items:center;justify-content:center}
.person{position:absolute;left:108px;top:344px;color:var(--white)}
.person-name{font-size:30px}
.person-role{font-size:19px;margin-top:2px}

/* newsletter & footer */
.footer{left:0;top:2883px;width:1200px;height:542px;background:var(--footer)}
.news{left:189px;top:2771px;width:797px;height:181px;background:var(--steel);border-radius:4px}
.news-text{position:absolute;left:0;width:100%;top:33px;text-align:center;font-size:23px;color:var(--white)}
.news-form{position:absolute;left:162px;top:96px;width:454px;height:48px;background:var(--white);border-radius:6px}
.news-input{position:absolute;left:15px;top:16px;font-size:12px;color:#555}
.news-btn{position:absolute;left:289px;top:5px;width:162px;height:38px;border-radius:20px;background:var(--teal);color:var(--white);font-size:19px;font-weight:500;display:flex;align-items:center;justify-content:center}
.foot-brand{left:53px;top:3070px;display:flex;align-items:center;gap:10px;font-size:26px;font-weight:500;color:var(--white)}
.foot-brand .brand-mark{background:var(--white)}
.foot-tag{left:52px;top:3140px;font-size:19px;line-height:31px;color:var(--white)}
.social{left:49px;top:3263px;display:flex;gap:12px}
.social span{width:28px;height:28px;border:2px solid var(--white);border-radius:50%}
.foot-col{top:3018px;color:var(--white)}
.foot-col h4{font-size:26px;font-weight:400;margin-bottom:22px}
.foot-col li{list-style:none;font-size:19px;line-height:31px}
.foot-rule{left:47px;top:3348px;width:1106px;height:1px;background:rgba(255,255,255,.5)}
.copy{left:0;width:1200px;top:3376px;text-align:center;font-size:19px;color:var(--white)}
</style>
</head>
<body>

<section class="hero abs">
  <div class="hero-art abs" role="img" aria-label="Illustration of learners around a large laptop with video player, books, ladder and magnifying glass"></div>
  <svg class="hero-wave abs" width="1200" height="152" viewBox="0 0 1200 152">
    <path d="M440 152 C470 60 560 20 680 60 C760 90 800 60 900 40 C1000 20 1080 10 1200 20 L1200 152 Z" fill="#a8e3cf" opacity=".7"/>
    <path d="M0 120 C300 140 500 130 700 125 C900 120 1050 110 1200 95 L1200 152 L0 152 Z" fill="var(--teal)"/>
    <path d="M0 152 C300 130 600 130 1200 140 L1200 152 Z" fill="#fff"/>
  </svg>
</section>

<div class="brand abs"><span class="brand-mark"></span>Velmont Data</div>
<nav class="nav abs">
  <a style="left:0">Explore</a>
  <a style="left:120px">Courses</a>
  <a style="left:247px">Pricing</a>
  <a style="left:372px">Blog</a>
</nav>
<a class="btn-sign btn-signin abs">Sign In</a>
<a class="btn-sign btn-signup abs">Sign Up</a>

<h1 class="hero-title abs">Provide best Learning<br>Experience for Architect</h1>
<p class="hero-sub abs">Learn to cloud with fun courses and labs taught<br>by the industry's experts.</p>
<p class="hero-label abs">FOR INDIVIDUALS</p>
<a class="hero-cta btn-teal abs">Start a 7-Day Free Trial</a>

<section>
  <div class="indiv-art abs" role="img" aria-label="Illustration of an instructor presenting on a screen to a learner at a laptop, with a stack of books"></div>
  <h2 class="indiv-title abs">Velmont for Individual Use</h2>
  <p class="indiv-text abs">Get access to our library of Cloud Courses and prepare for<br>multiple certifications. You get the flexibility to train on your<br>own terms so you can take your certifications when you're<br>ready.</p>
  <ul class="checks indiv-list abs">
    <li><svg width="17" height="17"><circle cx="8.5" cy="8.5" r="8.5" fill="var(--teal)"/><path d="M4.5 8.8l2.8 2.7 5-5" stroke="#fff" stroke-width="2" fill="none"/></svg>Flexibility to train on your own terms</li>
    <li><svg width="17" height="17"><circle cx="8.5" cy="8.5" r="8.5" fill="var(--teal)"/><path d="M4.5 8.8l2.8 2.7 5-5" stroke="#fff" stroke-width="2" fill="none"/></svg>Unlimited access to all our Cloud Courses</li>
    <li><svg width="17" height="17"><circle cx="8.5" cy="8.5" r="8.5" fill="var(--teal)"/><path d="M4.5 8.8l2.8 2.7 5-5" stroke="#fff" stroke-width="2" fill="none"/></svg>Train for multiple certifications</li>
    <li><svg width="17" height="17"><circle cx="8.5" cy="8.5" r="8.5" fill="var(--teal)"/><path d="M4.5 8.8l2.8 2.7 5-5" stroke="#fff" stroke-width="2" fill="none"/></svg>Stay up-to-date with the latest in Cloud Development</li>
    <li><svg width="17" height="17"><circle cx="8.5" cy="8.5" r="8.5" fill="var(--teal)"/><path d="M4.5 8.8l2.8 2.7 5-5" stroke="#fff" stroke-width="2" fill="none"/></svg>No hassle monthly payment</li>
  </ul>
  <a class="indiv-cta btn-teal abs">Start Learning Cloud Today</a>
</section>

<section>
  <svg class="tracks-band abs" width="1200" height="700" viewBox="0 0 1200 700">
    <path d="M0 60 C200 0 500 20 800 50 C1000 70 1100 40 1200 30 L1200 640 C900 650 400 660 0 690 Z" fill="var(--mint)" opacity=".7"/>
  </svg>
  <h3 class="track-head abs" style="left:40px">Programming Language</h3>
  <h3 class="track-head abs" style="left:505px">Cloud Service</h3>
  <h3 class="track-head abs" style="left:829px">Information Technology</h3>

  <article class="card abs" style="left:16px">
    <div class="card-art" role="img" aria-label="Illustration of a laptop showing code between glowing server blocks" style="background:linear-gradient(180deg,#f3eefc,#e6e0f7)"></div>
    <ul class="checks">
      <li><svg width="16" height="16"><circle cx="8" cy="8" r="8" fill="var(--teal)"/><path d="M4.2 8.3l2.6 2.5 4.7-4.7" stroke="#fff" stroke-width="2" fill="none"/></svg><span>Associate and Professional level<br>certification courses</span></li>
      <li><svg width="16" height="16"><circle cx="8" cy="8" r="8" fill="var(--teal)"/><path d="M4.2 8.3l2.6 2.5 4.7-4.7" stroke="#fff" stroke-width="2" fill="none"/></svg><span>Hands-on Labs and deep dive in<br>projects</span></li>
      <li><svg width="16" height="16"><circle cx="8" cy="8" r="8" fill="var(--teal)"/><path d="M4.2 8.3l2.6 2.5 4.7-4.7" stroke="#fff" stroke-width="2" fill="none"/></svg><span>Javascript programming language<br>and Vexo.js</span></li>
    </ul>
    <a class="card-btn btn-teal">Browse Courses</a>
  </article>

  <article class="card abs" style="left:411px">
    <div class="card-art" role="img" aria-label="Illustration of a cloud linked to a desktop computer and devices on a circuit pattern" style="background:linear-gradient(180deg,#f4f6fc,#e3ebfb)"></div>
    <ul class="checks">
      <li><svg width="16" height="16"><circle cx="8" cy="8" r="8" fill="var(--teal)"/><path d="M4.2 8.3l2.6 2.5 4.7-4.7" stroke="#fff" stroke-width="2" fill="none"/></svg><span>Certification and service deep dive<br>courses</span></li>
      <li><svg width="16" height="16"><circle cx="8" cy="8" r="8" fill="var(--teal)"/><path d="M4.2 8.3l2.6 2.5 4.7-4.7" stroke="#fff" stroke-width="2" fill="none"/></svg><span>Access all 10 VKT Certification<br>courses</span></li>
      <li><svg width="16" height="16"><circle cx="8" cy="8" r="8" fill="var(--teal)"/><path d="M4.2 8.3l2.6 2.5 4.7-4.7" stroke="#fff" stroke-width="2" fill="none"/></svg><span>Weekly updates on new<br>developments in the world of Lomen</span></li>
    </ul>
    <a class="card-btn btn-teal">Browse Courses</a>
  </article>

  <article class="card abs" style="left:805px">
    <div class="card-art" role="img" aria-label="Illustration of a laptop with floating dashboards and documents" style="background:linear-gradient(180deg,#f5f8fd,#e4ecf8)"></div>
    <ul class="checks">
      <li><svg width="16" height="16"><circle cx="8" cy="8" r="8" fill="var(--teal)"/><path d="M4.2 8.3l2.6 2.5 4.7-4.7" stroke="#fff" stroke-width="2" fill="none"/></svg><span>Fundamental Information<br>Technology Engineer</span></li>
      <li><svg width="16" height="16"><circle cx="8" cy="8" r="8" fill="var(--teal)"/><path d="M4.2 8.3l2.6 2.5 4.7-4.7" stroke="#fff" stroke-width="2" fill="none"/></svg><span>Information Security Management</span></li>
      <li><svg width="16" height="16"><circle cx="8" cy="8" r="8" fill="var(--teal)"/><path d="M4.2 8.3l2.6 2.5 4.7-4.7" stroke="#fff" stroke-width="2" fill="none"/></svg><span>Information Security Specialist</span></li>
    </ul>
    <a class="card-btn btn-teal">Browse Courses</a>
  </article>
</section>

<section>
  <h2 class="success-title abs">Proven Success</h2>

  <article class="quote-card abs" style="left:121px">
    <h3 class="quote-title">300 certifications in<br>12 months</h3>
    <p class="quote-text">“Velmont Data is just awesome - the perfect place to learn the best framework in the world! I love it!”</p>
    <svg class="quote-wave" width="451" height="133" viewBox="0 0 451 133"><path d="M0 35 C60 0 120 0 200 30 C290 62 380 70 451 50 L451 133 L0 133 Z" fill="var(--steel)"/></svg>
    <div class="avatar"><svg width="30" height="32" viewBox="0 0 30 32"><circle cx="15" cy="9" r="8" fill="var(--teal)"/><path d="M0 32 C0 20 30 20 30 32 Z" fill="var(--teal)"/></svg></div>
    <div class="person"><div class="person-name">John Doe</div><div class="person-role">&nbsp;-&nbsp; Managing Director</div></div>
  </article>

  <article class="quote-card abs" style="left:612px">
    <h3 class="quote-title">Developer Skill Set</h3>
    <p class="quote-text">“Velmont Data has been helpful in leveling up my skill-set in Qarl, but as a developer in general”</p>
    <svg class="quote-wave" width="451" height="133" viewBox="0 0 451 133"><path d="M0 35 C60 0 120 0 200 30 C290 62 380 70 451 50 L451 133 L0 133 Z" fill="var(--steel)"/></svg>
    <div class="avatar"><svg width="30" height="32" viewBox="0 0 30 32"><circle cx="15" cy="9" r="8" fill="var(--teal)"/><path d="M0 32 C0 20 30 20 30 32 Z" fill="var(--teal)"/></svg></div>
    <div class="person"><div class="person-name">Russell</div><div class="person-role">- Chief Operations</div></div>
  </article>
</section>

<footer>
  <div class="footer abs"></div>
  <div class="news abs">
    <p class="news-text">Want us to email you occasionally with Velmont’s news?</p>
    <div class="news-form"><span class="news-input">Enter your email address</span><span class="news-btn">SUBSCRIBE</span></div>
  </div>
  <div class="foot-brand abs"><span class="brand-mark"></span>Velmont Data</div>
  <p class="foot-tag abs">Provide best learning experience<br>to become a Software Architect.</p>
  <div class="social abs"><span></span><span></span><span></span></div>
  <div class="foot-col abs" style="left:456px">
    <h4>Training</h4>
    <ul><li>VKT Courses Online</li><li>Cloud Training</li><li>VKT Certifications</li><li>VKT Certified Solutions</li><li>Architect</li></ul>
  </div>
  <div class="foot-col abs" style="left:753px">
    <h4>Resources</h4>
    <ul><li>Discussions</li><li>Memberships</li><li>Blog</li><li>BSG on Inkwell</li><li>Support</li><li>VKT This Week</li><li>The Skycast</li></ul>
  </div>
  <div class="foot-col abs" style="left:1012px">
    <h4>About Us</h4>
    <ul><li>Our Story</li><li>Careers</li><li>Newsroom</li><li>Privacy</li><li>Terms</li></ul>
  </div>
  <div class="foot-rule abs"></div>
  <p class="copy abs">© Velmont Data 2020. All rights reserved.</p>
</footer>

</body>
</html>
```